Retirement Plan Advisor Bio

See the attached document and photo for content. I would like someone to design this one page flyer using my logo. This logo was designed by a designer with sketch hive. I am looking for a professional looking document. I want to he color scheme to be primarily white and gold.

Target Market(s)

Employers who offer a retirement plan

Requirements
Should not have
• The designs that I have received look more like resumes. I am interested in advertising my Retirement plan services. If anyone can change their submissions and change it to an ad for retirement plan services instead of a Bio or resume, I would prefer that.

```html
<!DOCTYPE html>
<html lang="en">
<head>
<meta charset="utf-8">
<title>Claire M. Halden – Retirement Plan Advisor</title>
<link rel="stylesheet" href="https://fonts.googleapis.com/css2?family=Open+Sans:wght@400;600;700&display=swap">
<style>
  :root {
    --gold: #c9a463;
    --gold-light: #d8b678;
    --gold-deep: #b08a4c;
    --brown-mid: #7d6848;
    --brown-dark: #3d342c;
    --white: #ffffff;
    --ink: #3a3a3a;
    --rule: #9a9a9a;
  }
  * { box-sizing: border-box; margin: 0; padding: 0; }
  html, body { width: 1083px; height: 1200px; overflow: hidden; background: #ffffff; }
  body { font-family: "Open Sans", Arial, sans-serif; }

  .flyer { position: relative; width: 1083px; height: 1200px; overflow: hidden; }

  .hero {
    position: absolute; left: 0; top: 0; width: 1083px; height: 870px;
    background:
      radial-gradient(ellipse 420px 320px at 470px 560px, rgba(160,140,110,0.45), transparent 70%),
      linear-gradient(180deg, var(--gold-deep) 0%, #a98a57 28%, var(--brown-mid) 55%, var(--brown-dark) 100%);
    color: var(--white);
  }
  .portrait-panel {
    position: absolute; left: 705px; top: 0; width: 270px; height: 310px;
    background: linear-gradient(180deg, var(--gold-light) 0%, rgba(210,175,115,0.55) 100%);
  }
  .portrait {
    position: absolute; left: 703px; top: 90px; width: 274px; height: 274px;
    border-radius: 50%; border: 6px solid var(--gold);
    background: radial-gradient(circle at 50% 40%, #d9c9a5 0%, #8f9fbf 60%, #5d6f95 100%);
  }

  .intro { position: absolute; left: 90px; top: 100px; width: 560px; }
  .name { font-size: 33px; font-weight: 700; line-height: 1.2; }
  .credentials { font-size: 18px; line-height: 1.4; margin-top: 6px; }
  .mission { font-size: 19px; line-height: 1.5; margin-top: 22px; text-align: justify; }
  .mission strong { font-weight: 700; }

  .details { position: absolute; left: 90px; top: 384px; width: 900px; }
  .section-title { font-size: 19px; font-weight: 700; line-height: 1.4; margin-top: 16px; }
  .section-title:first-child { margin-top: 0; }
  .list { list-style: none; font-size: 19px; line-height: 1.45; }
  .list li { position: relative; padding-left: 16px; text-align: justify; }
  .list li::before { content: "•"; position: absolute; left: 0; }
  .spaced { letter-spacing: 4px; }
  .disclosure { font-size: 18.5px; line-height: 1.45; padding-left: 16px; }

  .gold-band { position: absolute; left: 0; top: 870px; width: 1083px; height: 36px; background: var(--gold); }

  .footer { position: absolute; left: 0; top: 906px; width: 1083px; height: 294px; background: var(--white); }
  .contact { position: absolute; left: 120px; top: 52px; list-style: none; color: var(--ink); font-size: 21px; line-height: 1.45; }
  .contact li { display: flex; align-items: flex-start; gap: 16px; margin-bottom: 4px; }
  .contact svg { width: 20px; height: 20px; flex: none; margin-top: 5px; fill: none; stroke: var(--gold); stroke-width: 2; }
  .divider { position: absolute; left: 455px; top: 30px; width: 1px; height: 230px; background: var(--rule); }
  .brand { position: absolute; left: 520px; top: 112px; display: flex; align-items: center; gap: 16px; }
  .brand-mark { width: 30px; height: 30px; background: var(--gold); }
  .brand-name { font-size: 38px; font-weight: 600; color: var(--gold-deep); letter-spacing: 1px; }
</style>
</head>
<body>
<main class="flyer">
  <section class="hero">
    <div class="portrait-panel"></div>
    <div class="portrait" role="img" aria-label="Portrait photo of the advisor"></div>

    <header class="intro">
      <h1 class="name">About Claire M. Halden</h1>
      <p class="credentials">CFP®AIF®<br>Ridgepoint Financial Advisor</p>
      <p class="mission">I strive to improve retirement outcomes for my plan sponsor clients and their employees through careful retirement plan design assistance, strategic and targeted communication <strong>and education , as well as continual monitoring of results.</strong></p>
    </header>

    <div class="details">
      <h2 class="section-title">Professional Specialties</h2>
      <ul class="list">
        <li class="spaced">Over 18 years of experience in the retirement plan industry.</li>
        <li>Focused on helping plan sponsors reduce administrative burdens and fiduciary risk.</li>
        <li>Dedicated to helping employees work toward a positive retirement outcome through careful analysis of their savings rate, investment strategy and overall financial wellness.</li>
      </ul>

      <h2 class="section-title">Qualifications</h2>
      <ul class="list">
        <li>Certified Financial Planner®</li>
        <li>Accredited Investment Fiduciary®</li>
        <li>Investment Advisor Representative.</li>
        <li>Series 7, 63, and 65 Securities licenses with Ridgepoint Financial.</li>
        <li>Holds Life and Health Insurance licenses from Illinois.</li>
      </ul>

      <h2 class="section-title">Education</h2>
      <ul class="list">
        <li>BS Westbrook University, 1987.</li>
      </ul>
      <p class="disclosure">*Securities and Investment Advisory Services offered through Ridgepoint Financial Holdings, Inc, a Registered Broker/Dealer and Investment Advisor, member NSRA/IPF.</p>
    </div>
  </section>

  <div class="gold-band"></div>

  <footer class="footer">
    <ul class="contact">
      <li>
        <svg viewBox="0 0 20 20"><path d="M10 18s6-6.5 6-10.5A6 6 0 0 0 4 7.5C4 11.5 10 18 10 18z"/><circle cx="10" cy="7.5" r="2"/></svg>
        <span>240 Maple Grove Rd.<br>Fairview, IL 60400</span>
      </li>
      <li>
        <svg viewBox="0 0 20 20"><path d="M4 3h4l1.5 4-2 1.5a9 9 0 0 0 4 4l1.5-2 4 1.5v4a1.5 1.5 0 0 1-1.5 1.5A14 14 0 0 1 2.5 4.5 1.5 1.5 0 0 1 4 3z"/></svg>
        <span>(555)210.4830</span>
      </li>
      <li>
        <svg viewBox="0 0 20 20"><rect x="2" y="5" width="16" height="11"/><path d="M2 5l8 6 8-6"/></svg>
        <span>claire.halden@ridgepoint.com</span>
      </li>
      <li>
        <svg viewBox="0 0 20 20"><circle cx="10" cy="10" r="8"/><ellipse cx="10" cy="10" rx="3.5" ry="8"/><path d="M2 10h16"/></svg>
        <span>www.clairehalden.com</span>
      </li>
    </ul>
    <div class="divider"></div>
    <div class="brand">
      <span class="brand-mark"></span>
      <span class="brand-name">Keystone Wealth, LLC</span>
    </div>
  </footer>
</main>
</body>
</html>
```